Insight Plus. needs Business Cards

For this project, we need business cards (currently have also put a call out for a logo). We are a start-up called Insight Plus. This is our second company (our first one was called Querivance). Traditionally we have been providing market research services across different sectors, primarily financial services and the pharmaceutical industry. However, we now want to go beyond market research to offer more (Plus.)... strategic consulting and big data knowledge management. We want our brand to be approachable, creative, fun but professional.

Target Market(s)

The target audience is a business professional - we are B2B (business to business) and do not sell our services to individuals. The brands we work with are major brands across industries, but primarily automotive, financial and pharmaceutical.

Industry/Entity Type

Market Research

Font styles to use
Serif
Sans Serif
Other font styles liked:
• Calibri

Requirements
Must have
• Be clean, simple, modern
Show our address and phone number and email address and website URL
We do not need to have titles showing.

```html
<!DOCTYPE html>
<html lang="en">
<head>
<meta charset="utf-8">
<title>Insight Plus. – Business Cards</title>
<link rel="stylesheet" href="https://fonts.googleapis.com/css2?family=Carlito:ital,wght@0,400;0,700;1,700&display=swap">
<style>
  :root {
    --backdrop: #8c8c8c;
    --card: #f2f2f0;
    --brand-red: #6e0010;
    --bar-grey: #6a6a68;
    --ink: #141414;
    --wordmark-ink: #2a2a2a;
    --name-ink: #ececec;
  }
  * { margin: 0; padding: 0; box-sizing: border-box; }
  html, body {
    width: 1200px;
    height: 1000px;
    overflow: hidden;
    background: var(--backdrop);
    font-family: "Carlito", Calibri, Arial, sans-serif;
  }
  .canvas {
    position: relative;
    width: 1200px;
    height: 1000px;
  }
  .card {
    position: absolute;
    left: 250px;
    width: 700px;
    height: 400px;
    background: var(--card);
    border-radius: 3px;
    box-shadow: 0 6px 18px rgba(0,0,0,0.25);
    overflow: hidden;
  }
  .card--back { top: 60px; }
  .card--front { top: 540px; }

  .band {
    position: absolute;
    left: 0;
    background: var(--brand-red);
    display: flex;
    align-items: center;
  }
  .card--back .band {
    top: 80px;
    width: 580px;
    height: 120px;
  }
  .card--front .band {
    top: 130px;
    width: 400px;
    height: 110px;
  }
  .wordmark {
    margin-left: 110px;
    font-size: 50px;
    font-weight: 700;
    color: var(--wordmark-ink);
    letter-spacing: 0.5px;
  }
  .holder-name {
    margin-left: 88px;
    font-size: 44px;
    font-weight: 700;
    font-style: italic;
    color: var(--name-ink);
  }

  .bars {
    position: absolute;
    display: flex;
    flex-direction: column;
  }
  .bars span {
    display: block;
    background: var(--bar-grey);
  }
  .card--back .bars {
    left: 592px;
    top: 122px;
    gap: 12px;
  }
  .card--back .bars span { width: 100px; height: 18px; }
  .card--front .bars {
    left: 578px;
    top: 248px;
    gap: 13px;
  }
  .card--front .bars span { width: 112px; height: 22px; }

  .contact {
    position: absolute;
    left: 422px;
    top: 148px;
    list-style: none;
    font-size: 20px;
    line-height: 30px;
    color: var(--ink);
  }
</style>
</head>
<body>
  <main class="canvas">
    <section class="card card--back" aria-label="Card back">
      <div class="band">
        <span class="wordmark">Insight Plus.</span>
      </div>
      <div class="bars" aria-hidden="true">
        <span></span><span></span><span></span><span></span>
      </div>
    </section>

    <section class="card card--front" aria-label="Card front">
      <div class="band">
        <span class="holder-name">Your Name</span>
      </div>
      <ul class="contact">
        <li>P : 012- 345- 6789</li>
        <li>E : your name@mail.com</li>
        <li>W : www.address.com</li>
      </ul>
      <div class="bars" aria-hidden="true">
        <span></span><span></span><span></span><span></span>
      </div>
    </section>
  </main>
</body>
</html>
```